Trifold flyer for our dental clinic (the Bright Harbor Clinic)

The goal of this project is to design a trifold flyer for our dental clinic (the Bright Harbor Clinic). The winning design is expected to be creative, artistic and coherent with our logo.
Updates

Designs look the same

Target Market(s)

Young generation with dental need.

Industry/Entity Type

Dental Clinic

Font styles to use
Sans Serif

Colors
0355a3
85acd3
85cae6
0592cd
00a990
86cfc6
cedeed
cee9f5
cfeae6

Requirements
Must have
• See the attached sketch for content arrangement.

```html
<!DOCTYPE html>
<html lang="en">
<head>
<meta charset="utf-8">
<title>Bright Harbor Clinic – Trifold Flyer</title>
<link href="https://fonts.googleapis.com/css2?family=Open+Sans:wght@400;600;700&display=swap" rel="stylesheet">
<style>
  :root{
    --navy:#0a4f9c;
    --blue:#0355a3;
    --mid:#0592cd;
    --sky:#85cae6;
    --soft:#85acd3;
    --pale:#cee9f5;
    --mist:#cedeed;
    --white:#ffffff;
    --stage:#e8ecf0;
  }
  *{box-sizing:border-box;margin:0;padding:0}
  html,body{width:1200px;height:675px;overflow:hidden}
  body{background:var(--stage);font-family:"Open Sans",Arial,sans-serif;color:var(--white);position:relative}

  .spread{position:absolute;top:100px;width:570px;height:475px;display:flex;box-shadow:0 6px 18px rgba(0,0,0,.18)}
  .spread--inside{left:20px}
  .spread--outside{left:610px}
  .panel{position:relative;width:190px;height:100%;background:linear-gradient(180deg,var(--blue),var(--navy));padding:16px 13px;overflow:hidden;border-right:1px solid rgba(255,255,255,.08)}
  .panel:last-child{border-right:none}

  .heading{font-size:14px;font-weight:600;margin-bottom:7px}
  .note{font-size:7.5px;line-height:1.35;margin-bottom:6px}
  .sub{font-size:9px;line-height:1.35}
  .tier{font-size:9px;font-weight:600;margin:8px 0 4px;padding-bottom:2px;border-bottom:1px solid var(--sky);width:96px}

  .checks{list-style:none}
  .checks li{position:relative;padding-left:15px;font-size:7.5px;line-height:1.35;margin-bottom:6px}
  .checks li::before{content:"";position:absolute;left:0;top:1px;width:9px;height:9px;background:var(--white);border-radius:1px}
  .checks li::after{content:"";position:absolute;left:3px;top:2px;width:3px;height:5px;border:solid var(--blue);border-width:0 1.5px 1.5px 0;transform:rotate(45deg)}
  .checks--narrow{width:112px}

  .rings{list-style:none}
  .rings li{position:relative;padding-left:15px;font-size:7.5px;line-height:1.3;margin-bottom:6px}
  .rings li::before{content:"";position:absolute;left:0;top:1px;width:6px;height:6px;border:1.5px solid var(--white);border-radius:50%}
  .rings--services{width:114px}
  .rings--hours li{margin-bottom:5px}

  .photo{background:linear-gradient(135deg,var(--sky),var(--soft) 55%,var(--mid))}
  .photo--round{position:absolute;border-radius:50%;border:2px solid var(--white)}
  .photo--strip{height:74px;margin:6px -13px 10px;border-top:2px solid var(--white);border-bottom:2px solid var(--white)}

  .fee-box{border:1px solid var(--white);padding:4px 6px;font-size:7px;line-height:1.35;margin-top:8px}

  /* hours / address panel */
  .map-art{position:absolute;left:0;top:160px;width:190px;height:150px}
  .map-fill{position:absolute;left:0;top:182px;width:190px;height:100px;background:linear-gradient(160deg,var(--mist),var(--pale))}
  .address{position:absolute;left:13px;top:318px;right:10px}
  .contact-row{display:flex;align-items:center;gap:8px;font-size:7px;line-height:1.3;margin-bottom:7px}
  .contact-row svg{flex:none}

  /* team */
  .member{display:flex;gap:7px;margin-bottom:12px}
  .member .photo--round{position:static;flex:none;width:44px;height:44px}
  .member-name{font-size:8px;font-weight:700;margin-bottom:3px;text-transform:uppercase}
  .member-bio{font-size:6.8px;line-height:1.35}

  /* reviews */
  .reviews-panel{background:var(--blue)}
  .review{font-size:7px;line-height:1.4;margin-bottom:8px}
  .review strong{font-weight:700}
  .more{position:absolute;left:13px;right:13px;bottom:22px;font-size:7.5px;line-height:1.4}

  /* cover */
  .cover{padding:0}
  .cover-name{position:absolute;top:18px;left:0;right:0;text-align:center;font-size:13px;font-weight:600;letter-spacing:3px;line-height:1.3}
  .cover-art{position:absolute;top:60px;left:0;width:190px;height:130px}
  .cover-photo{position:absolute;top:60px;left:0;width:190px;height:108px;background:linear-gradient(135deg,var(--pale),var(--sky) 50%,var(--soft))}
  .tagline{position:absolute;top:200px;left:14px;line-height:1.05}
  .tagline .sm{font-size:11px}
  .tagline .lg{font-size:22px;font-weight:600}
  .offers{position:absolute;top:203px;right:10px;width:82px;border:1px solid var(--white);padding:4px 5px;font-size:5.8px;line-height:1.35}
  .offers b{display:block;font-size:7.5px;font-weight:600;margin-bottom:1px}
  .call{position:absolute;top:262px;left:14px;display:flex;align-items:center;gap:7px;font-size:10.5px;font-weight:700;letter-spacing:.4px}
  .cover-waves{position:absolute;left:0;bottom:0;width:190px;height:190px}
  .brand{position:absolute;left:0;right:0;bottom:40px;display:flex;flex-direction:column;align-items:center;gap:7px}
  .brand-dot{width:34px;height:34px;border-radius:50%;background:var(--sky)}
  .brand-name{font-size:9px;font-weight:600;color:var(--sky);letter-spacing:.5px}
</style>
</head>
<body>

<section class="spread spread--inside">

  <article class="panel">
    <h2 class="heading">Our Promos:</h2>
    <ul class="checks">
      <li>$69 New patient special exam, cleaning and digital X-ray. The Regular Price is $500.</li>
      <li>$99 In-office Teeth Whitening. Regular Price is $700.</li>
      <li>24%-40% Off on ClearFit aligners plus free consultation.</li>
    </ul>
    <div class="photo photo--strip" role="img" aria-label="Photo of a smiling young family"></div>
    <h2 class="heading">Our Services:</h2>
    <ul class="rings rings--services">
      <li>Cleaning and Prevention</li>
      <li>Cosmetic Dentistry</li>
      <li>Implant Dentistry</li>
      <li>Removable Dentures</li>
      <li>Orthodontics</li>
      <li>ClearFit aligners</li>
      <li>Pediatric Dentistry</li>
      <li>Multi-Specialty Treatment</li>
    </ul>
    <div class="photo photo--round" style="left:132px;top:238px;width:46px;height:46px" role="img" aria-label="Portrait photo of a smiling woman"></div>
    <div class="photo photo--round" style="left:132px;top:292px;width:46px;height:46px" role="img" aria-label="Portrait photo of a smiling young woman"></div>
  </article>

  <article class="panel">
    <h2 class="heading">Our Plans:</h2>
    <p class="note">Payout and financing options are available and most insurance accepted.</p>
    <p class="sub">No insurance?<br>Try our Dental Savings Plans:</p>

    <h3 class="tier">80%-100% Saving:</h3>
    <ul class="checks checks--narrow">
      <li>Preventive Dentistry</li>
      <li>Exam</li>
      <li>X-ray</li>
    </ul>
    <h3 class="tier">40%-80% Saving:</h3>
    <ul class="checks checks--narrow">
      <li>Dental Filling</li>
      <li>Dental Crowns</li>
      <li>In-Office Teeth Whiting</li>
    </ul>
    <h3 class="tier">25%-65% Saving:</h3>
    <ul class="checks checks--narrow">
      <li>Advanced Denture</li>
      <li>Dental Extraction</li>
      <li>Dental Braces</li>
    </ul>
    <div class="fee-box">Annual fee: $138<br>First Family member: $11.5/month</div>

    <div class="photo photo--round" style="left:130px;top:108px;width:48px;height:48px" role="img" aria-label="Photo of a laughing young woman"></div>
    <div class="photo photo--round" style="left:130px;top:186px;width:48px;height:48px" role="img" aria-label="Close-up photo of a bright smile"></div>
    <div class="photo photo--round" style="left:130px;top:258px;width:48px;height:48px" role="img" aria-label="Close-up photo of a smile with braces"></div>
  </article>

  <article class="panel">
    <h2 class="heading">Work Hoors:</h2>
    <ul class="rings rings--hours">
      <li>Sundays Closed</li>
      <li>Mondays Closed</li>
      <li>Tuesdays 9:30AM-5:00PM</li>
      <li>Wednesdays Closed</li>
      <li>Thursdays 9:30AM-5:00PM</li>
      <li>Fridays 9:00AM-5:00PM</li>
      <li>Saturdays 9:00AM-5:00PM</li>
    </ul>

    <svg class="map-art" viewBox="0 0 190 150" aria-hidden="true">
      <path d="M0 22 C50 -4 130 -4 190 14 L190 140 C130 120 60 122 0 150 Z" fill="var(--mist)"/>
      <path d="M0 22 C50 -4 130 -4 190 14" fill="none" stroke="var(--sky)" stroke-width="5"/>
      <path d="M0 150 C60 122 130 120 190 140" fill="none" stroke="var(--sky)" stroke-width="5"/>
    </svg>
    <div class="map-fill" role="img" aria-label="Street map showing the clinic location"></div>

    <div class="address">
      <h2 class="heading">Address:</h2>
      <div class="contact-row">
        <svg width="14" height="14" viewBox="0 0 14 14" aria-hidden="true"><rect x=".5" y=".5" width="13" height="13" fill="none" stroke="#fff"/><circle cx="7" cy="5" r="2.2" fill="#fff"/><path d="M3 12c0-3 8-3 8 0z" fill="#fff"/></svg>
        <span>240 Harbor Lane<br>Suite 12, Lakeview, MA 01000</span>
      </div>
      <div class="contact-row">
        <svg width="14" height="14" viewBox="0 0 14 14" aria-hidden="true"><rect x=".5" y=".5" width="13" height="13" fill="none" stroke="#fff"/><path d="M3 6c0-2 8-2 8 0l-1.5 1h-5z M4.5 7h5l1 4h-7z" fill="#fff"/></svg>
        <span>1-555-014-2210</span>
      </div>
      <div class="contact-row">
        <svg width="14" height="14" viewBox="0 0 14 14" aria-hidden="true"><rect x=".5" y=".5" width="13" height="13" fill="none" stroke="#fff"/><rect x="4" y="3" width="6" height="3" fill="#fff"/><rect x="2.5" y="6" width="9" height="4" fill="#fff"/><rect x="4" y="9" width="6" height="2.5" fill="none" stroke="#fff"/></svg>
        <span>1-555-014-2288</span>
      </div>
      <div class="contact-row">
        <svg width="14" height="14" viewBox="0 0 14 14" aria-hidden="true"><rect x=".5" y=".5" width="13" height="13" fill="none" stroke="#fff"/><rect x="2.5" y="4" width="9" height="6" fill="none" stroke="#fff"/><path d="M2.5 4l4.5 3.5 4.5-3.5" fill="none" stroke="#fff"/></svg>
        <span>info@brightharborclinic.example</span>
      </div>
      <div class="contact-row">
        <svg width="14" height="14" viewBox="0 0 14 14" aria-hidden="true"><rect x=".5" y=".5" width="13" height="13" fill="none" stroke="#fff"/><circle cx="7" cy="7" r="4.5" fill="none" stroke="#fff"/><ellipse cx="7" cy="7" rx="2" ry="4.5" fill="none" stroke="#fff"/><path d="M2.5 7h9" stroke="#fff"/></svg>
        <span>www.brightharborclinic.example</span>
      </div>
    </div>
  </article>
</section>

<section class="spread spread--outside">

  <article class="panel">
    <h2 class="heading" style="text-transform:uppercase">Our Team:</h2>
    <div class="member">
      <div class="photo photo--round" role="img" aria-label="Portrait photo of Dr. Dana Morrow"></div>
      <div>
        <h3 class="member-name">Dana Morrow, DMD, MS</h3>
        <p class="member-bio">Dr. Morrow earned her DMD and MS in orthodontics and leads our team with gentle care for every age.</p>
      </div>
    </div>
    <div class="member">
      <div class="photo photo--round" role="img" aria-label="Portrait photo of Dr. Owen R. Hale"></div>
      <div>
        <h3 class="member-name">Owen R. Hale, DMD</h3>
        <p class="member-bio">Dr. Hale is board certified in general dentistry and has treated families in our community for over fifteen years.</p>
      </div>
    </div>
    <div class="member">
      <div class="photo photo--round" role="img" aria-label="Portrait photo of Dr. Lena Brooks"></div>
      <div>
        <h3 class="member-name">Lena Brooks, DMD, MS</h3>
        <p class="member-bio">Dr. Brooks focuses on pediatric care and makes every young patient feel calm, safe and welcome in the chair.</p>
      </div>
    </div>
  </article>

  <article class="panel reviews-panel">
    <h2 class="heading">Reveiws:</h2>
    <p class="review">Feedback from <strong>Sam Porter</strong> on 2/10/2018<br>Great service. Everyone was so friendly!</p>
    <p class="review">Feedback from <strong>Nadia Reyes</strong> on 5/15/2018<br>Friendly staff, pleasant atmosphere, great on time and a very engaged doctor. Highly recommended!</p>
    <p class="review">Feedback from <strong>Priya Nolan</strong> on 2/10/2018<br>I have been coming to this facility for a year and I must say that it has been the best dental office I have ever been to. Dr Morrow makes me feel comfortable and explains every step. The staff is friendly, the office is clean and the waiting area is calm. I highly recommend this clinic to anyone looking for a caring team. Thank you for the amazing service!</p>
    <p class="more">For more Reviews Visit our website:<br>www.brightharborclinic.example</p>
  </article>

  <article class="panel cover">
    <h1 class="cover-name">BRIGHT HARBOR<br>CLINIC</h1>

    <svg class="cover-art" viewBox="0 0 190 130" aria-hidden="true">
      <path d="M0 0 H190 V112 C130 90 60 136 0 112 Z" fill="var(--sky)"/>
      <path d="M0 112 C60 136 130 90 190 112" fill="none" stroke="var(--mid)" stroke-width="5"/>
    </svg>
    <div class="cover-photo" role="img" aria-label="Photo of a group of smiling children"></div>

    <p class="tagline"><span class="sm">Your</span><br><span class="lg">smile</span> <span class="sm">is</span><br><span class="sm">Our passion</span></p>

    <div class="offers"><b>Special Offers:</b>$69 New Patients Special<br>$99 In-office teeth whitening<br>25%-40% off for ClearFit aligners</div>

    <p class="call">
      <svg width="16" height="12" viewBox="0 0 16 12" aria-hidden="true"><path d="M1 4c0-4 14-4 14 0l-3 1.5h-8z M4 5.5h8l2 6h-12z" fill="#fff"/><circle cx="8" cy="8.5" r="1.8" fill="var(--blue)"/></svg>
      CALL US: 555.014.2210
    </p>

    <svg class="cover-waves" viewBox="0 0 190 190" aria-hidden="true">
      <path d="M0 30 C60 0 120 60 190 30" fill="none" stroke="var(--mid)" stroke-width="6"/>
      <path d="M0 190 V150 C70 120 130 160 190 130 V190 Z" fill="var(--mid)"/>
      <path d="M0 170 C70 140 130 180 190 150 V190 H0 Z" fill="var(--sky)" opacity=".7"/>
    </svg>

    <div class="brand">
      <span class="brand-dot"></span>
      <span class="brand-name">BRIGHT HARBOR CLINIC</span>
    </div>
  </article>
</section>

</body>
</html>
```